serious, thorough, light and simple - that's my advice and mediations

My business card should combine my logo (uploaded file) and my homepage (https://fellor-mediation.webnestsite.com).

Contact Information for Business Card

Name: Sabine Fellor di Vanti
Phone: 076 412 58 94
mail: sfellor@postkiv.ch
web: www.fellor-di-vanti.ch

```html
<!DOCTYPE html>
<html lang="de">
<head>
<meta charset="utf-8">
<title>Leute im Wandel – Visitenkarte</title>
<link href="https://fonts.googleapis.com/css2?family=Poppins:wght@400;500&display=swap" rel="stylesheet">
<style>
  :root {
    --backdrop: #2a2b30;
    --card: #ffffff;
    --gold: #b08a4e;
    --green: #1f6f4a;
    --blue: #2b3f93;
  }
  * { margin: 0; padding: 0; box-sizing: border-box; }
  html, body { width: 1200px; height: 800px; overflow: hidden; }
  body {
    background: var(--backdrop);
    font-family: "Poppins", sans-serif;
    position: relative;
  }
  .card {
    position: absolute;
    top: 245px;
    width: 540px;
    height: 309px;
    background: var(--card);
    border-radius: 18px;
    box-shadow: 0 14px 30px rgba(0,0,0,0.35);
  }
  .card--front { left: 40px; }
  .card--back { left: 620px; }

  .brand__name {
    color: var(--gold);
    font-weight: 500;
    font-size: 30px;
    letter-spacing: 0.5px;
    white-space: nowrap;
  }
  .card--front .brand {
    position: absolute;
    left: 50%; top: 50%;
    transform: translate(-50%, -50%);
  }
  .card--back .brand {
    position: absolute;
    left: 40px; top: 196px;
  }
  .card--back .brand__name { font-size: 22px; }

  .divider {
    position: absolute;
    left: 290px; top: 92px;
    width: 1.5px; height: 130px;
    background: var(--green);
  }
  .contact {
    position: absolute;
    left: 308px; top: 96px;
  }
  .contact__name {
    color: var(--gold);
    font-size: 17px;
    font-weight: 400;
    margin-bottom: 10px;
    white-space: nowrap;
  }
  .contact__list { list-style: none; }
  .contact__item {
    display: flex;
    align-items: center;
    gap: 7px;
    color: var(--green);
    font-size: 12.5px;
    line-height: 1;
    margin-bottom: 8px;
    white-space: nowrap;
  }
  .contact__icon { width: 15px; height: 15px; flex: none; }
</style>
</head>
<body>
  <section class="card card--front" aria-label="Vorderseite">
    <div class="brand">
      <span class="brand__name">Leute im Wandel</span>
    </div>
  </section>

  <section class="card card--back" aria-label="Rückseite">
    <div class="brand">
      <span class="brand__name">Leute im Wandel</span>
    </div>
    <div class="divider"></div>
    <div class="contact">
      <p class="contact__name">Sabine Fellor di Vanti</p>
      <ul class="contact__list">
        <li class="contact__item">
          <svg class="contact__icon" viewBox="0 0 16 16" aria-hidden="true">
            <circle cx="8" cy="8" r="8" fill="var(--blue)"/>
            <rect x="5.5" y="3.5" width="5" height="9" rx="1" fill="none" stroke="#fff" stroke-width="1.1"/>
            <circle cx="8" cy="10.8" r="0.6" fill="#fff"/>
          </svg>
          076 412 58 94
        </li>
        <li class="contact__item">
          <svg class="contact__icon" viewBox="0 0 16 16" aria-hidden="true">
            <circle cx="8" cy="8" r="8" fill="var(--blue)"/>
            <rect x="4" y="5" width="8" height="6" fill="none" stroke="#fff" stroke-width="1.1"/>
            <path d="M4 5 L8 8.5 L12 5" fill="none" stroke="#fff" stroke-width="1.1"/>
          </svg>
          sfellor@postkiv.ch
        </li>
        <li class="contact__item">
          <svg class="contact__icon" viewBox="0 0 16 16" aria-hidden="true">
            <circle cx="8" cy="8" r="8" fill="var(--blue)"/>
            <circle cx="8" cy="8" r="4" fill="none" stroke="#fff" stroke-width="1"/>
            <path d="M4 8 H12 M8 4 C6 6 6 10 8 12 M8 4 C10 6 10 10 8 12" fill="none" stroke="#fff" stroke-width="0.9"/>
          </svg>
          www.fellor-di-vanti.ch
        </li>
      </ul>
    </div>
  </section>
</body>
</html>
```